Brochure Design Project

We are a manufacturing business based in Archerfield, Australia. We service the air conditioning industry. Our brochure will have some of our information and history on one side, followed by a list of products and services on the back.

Our current logo must be used.

Size will be

216mm x 279mm

Double sided.

Target Market(s)

air conditioning contractors

Industry/Entity Type

Air Conditioning

Requirements
Must have
• Must haves

Company history paragraph

Corvel Insulation Has been established in the HVAC industry since 1984. It has grown from 2 to 16 employees.

We pride ourselves on offering the fastest lagging service in Brisbane. With our new CNC machine we can meet any demands large or small.

services-
Internal and external insulating of HVAC ductwork
Manufacture of metal cushion boxes
Manufacture of ductboard cushion boxes
Cut and facing of insulation to size and shape.

Products-
glasswool insulation
ductboard
Closed cell foam
Sonthex
Ceramic board
variety of foils
metal spigots
pins and clips

Pictures of our products

Factory location-
47 Merrilong Street
Archerfield, QLD, 4152

Telephone number-
07 3190 4623

Email address-
ray@corvelinsulation.example.com.au

```html
<!DOCTYPE html>
<html lang="en">
<head>
<meta charset="utf-8">
<title>Corvel Insulation Brochure</title>
<link rel="stylesheet" href="https://fonts.googleapis.com/css2?family=Arimo:wght@400;700&display=swap">
<style>
  :root {
    --orange: #e8862e;
    --orange-deep: #d9701c;
    --orange-soft: #f3a35a;
    --grey-light: #eeeeee;
    --grey-mid: #d4d4d4;
    --grey-text: #6d6d6d;
    --white: #ffffff;
    --ink: #111111;
    --foam-yellow: #f2c24a;
    --foam-pale: #f8dc92;
  }
  * { margin: 0; padding: 0; box-sizing: border-box; }
  html, body { width: 1200px; height: 3027px; overflow: hidden; background: var(--white); }
  body { position: relative; font-family: "Arimo", Arial, sans-serif; }

  .page { position: absolute; left: 35px; width: 1130px; overflow: hidden; }
  .page-front { top: 33px; height: 1461px; background: var(--orange); }
  .page-back { top: 1523px; height: 1470px; background: var(--orange); }

  .front-art { position: absolute; inset: 0; }

  .history { position: absolute; left: 84px; top: 1150px; width: 520px;
    color: var(--white); font-size: 21px; line-height: 25px; }
  .history p + p { margin-top: 25px; }

  .brand { position: absolute; left: 620px; top: 1232px; display: flex; align-items: center; gap: 18px; }
  .brand-square { width: 54px; height: 54px; background: var(--orange); }
  .brand-name { font-size: 46px; font-weight: 700; color: var(--grey-text); letter-spacing: 1px; }

  .panel { position: absolute; left: 49px; width: 1029px; border-radius: 22px;
    background: linear-gradient(180deg, var(--grey-light) 0%, var(--white) 55%, var(--grey-light) 100%); }
  .panel-services { top: 66px; height: 237px; text-align: center; padding-top: 26px; }
  .panel-products { top: 325px; height: 780px; text-align: center; padding-top: 30px; }
  .panel-title { color: var(--orange); font-weight: 700; font-size: 38px; line-height: 44px; }
  .service-list { list-style: none; color: var(--orange); font-size: 26px; line-height: 29px; }

  .product { position: absolute; width: 407px; height: 128px; border-radius: 12px; overflow: hidden; background: var(--white); }
  .product-photo { position: absolute; inset: 0; }
  .product-label { position: absolute; right: 0; bottom: 0; width: 294px; height: 38px;
    background: var(--orange); border-top-left-radius: 8px; color: var(--white);
    font-weight: 700; font-size: 23px; line-height: 38px; padding-left: 16px; text-align: left; }
  .col-a { left: 84px; }
  .col-b { left: 540px; }
  .row-1 { top: 91px; }
  .row-2 { top: 251px; }
  .row-3 { top: 408px; }
  .row-4 { top: 565px; }

  .back-base { position: absolute; left: 0; top: 0; width: 1130px; height: 1470px; }

  .contact { position: absolute; left: 0; top: 1106px; width: 1130px; text-align: center; color: var(--ink); }
  .contact-lines { font-weight: 700; font-size: 21px; line-height: 25px; }
  .contact-address { margin-top: 26px; font-size: 21px; }

  .map { position: absolute; left: 292px; top: 1233px; width: 545px; height: 171px;
    border: 5px solid var(--ink);
    background: linear-gradient(135deg, #cfe3b8 0%, #e9e6d8 45%, #d6e6c4 100%); }
</style>
</head>
<body>

<section class="page page-front">
  <svg class="front-art" viewBox="0 0 1130 1461" width="1130" height="1461" aria-hidden="true">
    <defs>
      <linearGradient id="front-lower" x1="0" y1="0" x2="1" y2="0">
        <stop offset="0" stop-color="#e8862e"/>
        <stop offset="0.45" stop-color="#ec9a50"/>
        <stop offset="0.75" stop-color="#e9e3dc"/>
        <stop offset="1" stop-color="#e4e4e4"/>
      </linearGradient>
    </defs>
    <rect width="1130" height="1461" fill="url(#front-lower)"/>
    <path d="M0,690 Q420,1060 1130,1150" fill="none" stroke="#ffffff" stroke-opacity="0.7" stroke-width="6"/>
    <path d="M0,675 Q430,1030 1130,1135 L1130,1165 Q430,1070 0,700 Z" fill="#e07a24"/>
  </svg>
  <svg class="front-art" viewBox="0 0 1130 1461" width="1130" height="1461" role="img" aria-label="Close-up photograph of a yellow glasswool insulation slab">
    <defs>
      <linearGradient id="foam" x1="0" y1="0" x2="1" y2="1">
        <stop offset="0" stop-color="#f2c24a"/>
        <stop offset="0.55" stop-color="#f5cf6a"/>
        <stop offset="1" stop-color="#f8dc92"/>
      </linearGradient>
    </defs>
    <path d="M0,0 H1130 V1125 Q430,1020 0,664 Z" fill="url(#foam)"/>
  </svg>

  <div class="history">
    <p>Corvel Insulation Has been established in the HVAC industry since 1984.<br>It has grown from 2 to 16 employees.</p>
    <p>We pride ourselves on offering the fastest lagging service in Brisbane. With our new CNC machine we can meet any demands large or small.</p>
  </div>

  <div class="brand">
    <span class="brand-square"></span>
    <span class="brand-name">Corvel Insulation</span>
  </div>
</section>

<section class="page page-back">
  <svg class="back-base" viewBox="0 0 1130 1470" width="1130" height="1470" aria-hidden="true">
    <defs>
      <linearGradient id="base-grey" x1="0" y1="0" x2="0" y2="1">
        <stop offset="0" stop-color="#ffffff"/>
        <stop offset="1" stop-color="#cfcfcf"/>
      </linearGradient>
    </defs>
  </svg>

  <div class="panel panel-services">
    <h2 class="panel-title">Services</h2>
    <ul class="service-list">
      <li>Internal and external insulating of HVAC ductwork</li>
      <li>Manufacture of metal cushion boxes</li>
      <li>Manufacture of ductboard cushion boxes</li>
      <li>Cut and facing of insulation to size and shape.</li>
    </ul>
  </div>

  <div class="panel panel-products">
    <h2 class="panel-title">Products</h2>

    <div class="product col-a row-1">
      <div class="product-photo" role="img" aria-label="Stacked yellow glasswool insulation sheets" style="background:linear-gradient(90deg,#e8d66a,#c9a94c)"></div>
      <span class="product-label">Glasswool insulation</span>
    </div>
    <div class="product col-b row-1">
      <div class="product-photo" role="img" aria-label="Metal ductwork fittings" style="background:linear-gradient(90deg,#9aa0a6,#d7dadd)"></div>
      <span class="product-label">Ductboard</span>
    </div>
    <div class="product col-a row-2">
      <div class="product-photo" role="img" aria-label="Dark grey closed cell foam sheet" style="background:linear-gradient(90deg,#5d6a73,#3c4750)"></div>
      <span class="product-label">Closed cell foam</span>
    </div>
    <div class="product col-b row-2">
      <span class="product-label">Sonthex</span>
    </div>
    <div class="product col-a row-3">
      <span class="product-label">Ceramic board</span>
    </div>
    <div class="product col-b row-3">
      <div class="product-photo" role="img" aria-label="Perforated metal foil sheet" style="background:linear-gradient(90deg,#6f7378,#a9adb2)"></div>
      <span class="product-label">Variety of foils</span>
    </div>
    <div class="product col-a row-4">
      <div class="product-photo" role="img" aria-label="Galvanised metal spigot" style="background:linear-gradient(90deg,#c9ccd0,#8e9399)"></div>
      <span class="product-label">Metal spigots</span>
    </div>
    <div class="product col-b row-4">
      <div class="product-photo" role="img" aria-label="Insulation pins and clips" style="background:linear-gradient(90deg,#7f8fa8,#b6c0cf)"></div>
      <span class="product-label">Pins and clips</span>
    </div>
  </div>

  <svg class="back-base" viewBox="0 0 1130 1470" width="1130" height="1470" aria-hidden="true">
    <defs>
      <linearGradient id="footer-grey" x1="0" y1="0" x2="0" y2="1">
        <stop offset="0" stop-color="#ffffff"/>
        <stop offset="1" stop-color="#c9c9c9"/>
      </linearGradient>
    </defs>
    <path d="M0,1222 Q565,878 1130,1222 V1470 H0 Z" fill="#d9701c"/>
    <path d="M0,1240 Q565,900 1130,1240 V1470 H0 Z" fill="url(#footer-grey)"/>
  </svg>

  <div class="contact">
    <div class="contact-lines">
      <p>T. 07 3190 4623</p>
      <p>E. ray@corvelinsulation.example.com.au</p>
    </div>
    <p class="contact-address">47 Merrilong Street, Archerfield, QLD, 4152</p>
  </div>

  <div class="map" role="img" aria-label="Street map showing the factory location in Archerfield"></div>
</section>

</body>
</html>
```